Skin Care Product Line needs custom designed labels

We need one to two label design templates that can be used across our natural skin care products such as body lotion, salt scrubs, lip balms, handmade soaps, body creams, body mists, foot creams, bath salts. The design will come in different colors. We have our own logo; however the logo should have the flower colored golden along with the word tavin.
Label sizes are :
1) 6 inches by 4 inches rectangular for body lotion,
2) 81/2 inches by 2 inches rectangular for body scrub,
3) 5 inches by 3 inches rectangular for body mist,
4) 2 inches by 3 inches for bath salts,
5) 2.125 inches by 2.125 inches for lip balm,
6) 11/2 inches by 1/12 inches label for soap.
Updates

The design should have a beige background with one color or two of the same colors for instance light lavender and a darker lavender. It should have a vintage feel to it because it's for a natural skin care line not commercial type. Also the fonts should be vintage looking. We can have one design with different colors such as light green, light yellow, light pink, light blue , light orange to go with the different scents. Added Tuesday, January 26, 2016

Target Market(s)

Young adults and aging boomers

Industry/Entity Type

Skin Care Product

Font styles to use
Decorative

Colors
cfeae6
b7a5cd
e4daeb
fbf289
fac994
9bcb3b
f9d9e8
f04a50
f68d4c

Requirements
Must have
• Please see attached image for design sample. Original Label design should have beige to tan colored background similar to the attached file. light colors such as lavender, light yellow, light orange, etc can be changed once original label is designed. We would need to be able to edit label design text and label design colors to match our different scents after we decide on the design.

```html
<!DOCTYPE html>
<html lang="en">
<head>
<meta charset="utf-8">
<title>Verdelle tavin – Hand &amp; Body Lotion Label</title>
<link href="https://fonts.googleapis.com/css2?family=Old+Standard+TT:wght@400;700&family=Open+Sans:wght@400&display=swap" rel="stylesheet">
<style>
  :root {
    --canvas-bg: #e9e9e9;
    --label-bg: #efece8;
    --ink: #2f2f2f;
    --ink-soft: #6b6b6b;
    --ornament-tone: #c9c6c2;
    --gold: #d9b42f;
  }
  * { box-sizing: border-box; margin: 0; padding: 0; }
  html, body {
    width: 1200px; height: 1200px; overflow: hidden;
    background: var(--canvas-bg);
  }
  .label {
    position: absolute; left: 290px; top: 122px;
    width: 620px; height: 955px;
    background: var(--label-bg);
    color: var(--ink);
    font-family: "Old Standard TT", "Times New Roman", serif;
    box-shadow: 0 2px 10px rgba(0,0,0,0.08);
  }
  .label__frame { position: absolute; inset: 0; }
  .corner-ornament {
    position: absolute; width: 110px; height: 110px;
    background: var(--ornament-tone); border-radius: 6px; opacity: .55;
  }
  .corner-ornament--tl { left: 34px; top: 34px; }
  .corner-ornament--tr { right: 34px; top: 34px; }
  .corner-ornament--bl { left: 34px; bottom: 34px; }
  .corner-ornament--br { right: 34px; bottom: 34px; }
  .centered { position: absolute; left: 0; width: 100%; text-align: center; }
  .brand {
    top: 200px; font-size: 46px; letter-spacing: 1px;
    display: flex; justify-content: center; align-items: center; gap: 14px;
  }
  .brand__dot { width: 20px; height: 20px; border-radius: 50%; background: var(--gold); }
  .brand__name { color: var(--ink); font-weight: 400; }
  .category {
    top: 354px; font-size: 24px; font-weight: 700; letter-spacing: 2px;
  }
  .divider-ornament {
    position: absolute; left: 50%; transform: translateX(-50%);
    width: 250px; height: 40px; background: var(--ornament-tone);
    border-radius: 20px; opacity: .6;
  }
  .divider-ornament--above { top: 410px; }
  .divider-ornament--below { top: 528px; }
  .divider-ornament--small { top: 690px; width: 230px; height: 50px; }
  .title-rule {
    position: absolute; left: 90px; width: 440px; height: 0;
    border-top: 1.5px solid var(--ink-soft);
  }
  .title-rule--top { top: 462px; }
  .title-rule--bottom { top: 514px; }
  .product-name {
    top: 467px; left: 90px; width: 440px;
    font-size: 33px; line-height: 42px; font-weight: 700; letter-spacing: .5px;
    white-space: nowrap;
  }
  .description {
    top: 598px; padding: 0 90px;
    font-family: "Open Sans", Arial, sans-serif;
    font-size: 16px; line-height: 1.55; color: var(--ink);
  }
  .net-weight {
    top: 806px; font-size: 28px; font-weight: 700; letter-spacing: 1.5px;
  }
</style>
</head>
<body>
  <main class="label">
    <svg class="label__frame" width="620" height="955" viewBox="0 0 620 955" aria-hidden="true">
      <rect x="22" y="22" width="576" height="911" fill="none" stroke="#4a4a4a" stroke-width="2"/>
      <rect x="30" y="30" width="560" height="895" fill="none" stroke="#8a8a8a" stroke-width="1"/>
      <line x1="170" y1="65" x2="450" y2="65" stroke="#4a4a4a" stroke-width="1.5"/>
      <line x1="170" y1="897" x2="450" y2="897" stroke="#4a4a4a" stroke-width="1.5"/>
      <line x1="52" y1="210" x2="52" y2="745" stroke="#4a4a4a" stroke-width="1.5"/>
      <line x1="568" y1="210" x2="568" y2="745" stroke="#4a4a4a" stroke-width="1.5"/>
      <g fill="#4a4a4a">
        <rect x="305" y="60" width="10" height="10" transform="rotate(45 310 65)"/>
        <rect x="305" y="892" width="10" height="10" transform="rotate(45 310 897)"/>
        <rect x="47" y="472" width="10" height="10" transform="rotate(45 52 477)"/>
        <rect x="563" y="472" width="10" height="10" transform="rotate(45 568 477)"/>
      </g>
    </svg>

    <div class="corner-ornament corner-ornament--tl" role="img" aria-label="Vintage scroll flourish ornament, top left corner"></div>
    <div class="corner-ornament corner-ornament--tr" role="img" aria-label="Vintage scroll flourish ornament, top right corner"></div>
    <div class="corner-ornament corner-ornament--bl" role="img" aria-label="Vintage scroll flourish ornament, bottom left corner"></div>
    <div class="corner-ornament corner-ornament--br" role="img" aria-label="Vintage scroll flourish ornament, bottom right corner"></div>

    <div class="centered brand">
      <span class="brand__name">Verdelle tavin</span>
      <span class="brand__dot"></span>
    </div>

    <p class="centered category">AROMATHERAPY</p>

    <div class="divider-ornament divider-ornament--above" role="img" aria-label="Decorative scroll divider above the product name"></div>
    <div class="title-rule title-rule--top"></div>
    <h1 class="centered product-name">HAND &amp; BODY LOTION</h1>
    <div class="title-rule title-rule--bottom"></div>
    <div class="divider-ornament divider-ornament--below" role="img" aria-label="Decorative scroll divider below the product name"></div>

    <p class="centered description">Luxurious moisturizing lotion infused with essential oils to help you ease into your moments of serenity.</p>

    <div class="divider-ornament divider-ornament--small" role="img" aria-label="Small decorative flourish ornament"></div>

    <p class="centered net-weight">8 fl oz - 226g</p>
  </main>
</body>
</html>
```